Podcast cover art for Steady Footing Podcast for Busy Mothers

I am relaunching my 3 year podcast under a new name. The podcast is called Steady Footing for Busy Mothers. The parent company is called Bright Path Living (see attached logo) and should be represented on the cover in a small way. Previously the show was called Bright Path Living. We talk about creating life balance for working moms by focusing on faith, marriage, parenting, career, health, home, finances, and friends/fun. I don't mind having stock photography on the cover but I prefer not to have my image on it as it is not a personal brand. I have attached a couple of stock images as inspiration.

Target Market(s)

working Christian moms age 30-45 income 75,000+, working full time, Christian faith, married

Industry/Entity Type

Media

Font styles to use
Serif

Requirements
Must have
• Podcast name: Steady Footing for Busy Mothers
• By: Bright Path Living (include logo)
• I also included my brand sheet for reference which includes my brand colors and fonts. Navy should be the primary with orange and gray as the accents
Should not have
• No flowers, or overly girly. My brand is more clean, preppy, and young-sophisticated.

```html
<!DOCTYPE html>
<html lang="en">
<head>
<meta charset="utf-8">
<title>Steady Footing for Busy Mothers – Podcast Cover</title>
<link rel="stylesheet" href="https://fonts.googleapis.com/css2?family=Cormorant+Garamond:ital,wght@0,500;1,500&family=Montserrat:wght@500&display=swap">
<style>
  :root {
    --slate: #5a6b7b;
    --paper: #ffffff;
    --accent: #f26a1b;
    --ink-dark: #2a3139;
    --divider: #4a5867;
    --icon: #f3f3f3;
    --photo-desk: linear-gradient(160deg, #dfe3e7 0%, #9aa7b5 55%, #5f7b9c 100%);
    --photo-family: linear-gradient(120deg, #f4f4f4 0%, #e9e6e3 45%, #c9b7a8 70%, #2f3642 100%);
  }
  html, body {
    margin: 0;
    padding: 0;
    overflow: hidden;
  }
  body {
    width: 1200px;
    height: 1200px;
  }
  .cover {
    position: relative;
    width: 1200px;
    height: 1200px;
    background: var(--slate);
    overflow: hidden;
  }
  .print {
    position: absolute;
    background: var(--paper);
    box-shadow: 0 6px 18px rgba(0, 0, 0, 0.18);
  }
  .print__photo {
    position: absolute;
  }
  .print--desk {
    left: -80px;
    top: -70px;
    width: 440px;
    height: 630px;
    transform: rotate(-3deg);
  }
  .print--desk .print__photo {
    left: 60px;
    top: 60px;
    width: 300px;
    height: 450px;
    background: var(--photo-desk);
  }
  .print--family {
    left: 420px;
    top: 80px;
    width: 900px;
    height: 700px;
    transform: rotate(4deg);
    transform-origin: 0 0;
  }
  .print--family .print__photo {
    left: 48px;
    top: 48px;
    width: 852px;
    height: 570px;
    background: var(--photo-family);
  }
  .sparkles {
    position: absolute;
    left: 0;
    top: 590px;
  }
  .title {
    position: absolute;
    left: 78px;
    top: 820px;
    margin: 0;
    font-family: "Cormorant Garamond", Georgia, serif;
    font-style: italic;
    font-weight: 500;
    font-size: 80px;
    line-height: 118px;
    color: var(--paper);
  }
  .byline {
    position: absolute;
    left: 85px;
    top: 1118px;
    display: flex;
    align-items: baseline;
    gap: 34px;
  }
  .byline__label {
    font-family: "Montserrat", Arial, sans-serif;
    font-weight: 500;
    font-size: 20px;
    letter-spacing: 4px;
    color: var(--accent);
  }
  .byline__brand {
    font-family: "Cormorant Garamond", Georgia, serif;
    font-weight: 500;
    font-size: 40px;
    color: var(--ink-dark);
  }
  .divider {
    position: absolute;
    left: 942px;
    top: 945px;
    width: 2px;
    height: 225px;
    background: var(--divider);
  }
  .briefcase {
    position: absolute;
    left: 960px;
    top: 955px;
  }
</style>
</head>
<body>
<main class="cover">
  <div class="print print--desk">
    <div class="print__photo" role="img" aria-label="Stock photo of hands typing on a laptop at a desk, blue shirt sleeve and wristwatch"></div>
  </div>

  <div class="print print--family">
    <div class="print__photo" role="img" aria-label="Stock photo of a mother in a business suit on the phone, playing with her baby on a white sofa"></div>
  </div>

  <svg class="sparkles" width="120" height="240" viewBox="0 0 120 240" aria-hidden="true">
    <g fill="none" stroke="var(--accent)" stroke-width="5" stroke-linejoin="round">
      <path d="M62 12 Q70 52 98 60 Q70 68 62 108 Q54 68 26 60 Q54 52 62 12 Z"/>
      <path d="M24 140 Q29 168 48 174 Q29 180 24 206 Q19 180 0 174 Q19 168 24 140 Z"/>
    </g>
  </svg>

  <h1 class="title">Steady Footing for<br>Busy Mothers</h1>

  <div class="byline">
    <span class="byline__label">BY</span>
    <span class="byline__brand">Bright Path Living</span>
  </div>

  <div class="divider"></div>

  <svg class="briefcase" width="200" height="190" viewBox="0 0 200 190" aria-label="Briefcase icon" role="img">
    <rect x="65" y="8" width="70" height="54" rx="10" fill="none" stroke="var(--icon)" stroke-width="16"/>
    <rect x="3" y="50" width="190" height="135" rx="16" fill="var(--icon)"/>
  </svg>
</main>
</body>
</html>
```